Letterhead for a German Distribution/Manufacturing Company

We need a professional Letterhead in a unique Design.
not to playful.
The Letterhead has to show show that we are a international company with headquater in Germany.
all details like adress, Vat Tax Number, Bank Accout, Eori, email, Company number has to be on the Letterhead.
for example use: VAT TAX DE5704168 Bank Account: Norrfeld Bank IBAN DE421705238ß310482 Swift: KOLV3154802 EORI 3041296587 Company Number: HRB 61508 Adress: VOLTRINA UG Amsel Strasse 7 Postal Code 04683 City Burgstädt Country: Germany Email: info@voltrina-example.com
the design can be colored but doesnt have to be
Industry/Entity Type
Manufacturing and international distribution
Requirements
Must have
- show that we are a international company with headquater in Germany. our company infos and logo

```html
<!DOCTYPE html>
<html lang="de">
<head>
<meta charset="utf-8">
<title>VOLTRINA UG – Letterhead</title>
<link rel="stylesheet" href="https://fonts.googleapis.com/css2?family=Montserrat:wght@400;500;600;800&display=swap">
<style>
  :root {
    --paper: #ffffff;
    --red: #c8161d;
    --red-icon: #e0242b;
    --ink: #141414;
    --gold: #f2b705;
    --rule: #2a2a2a;
    --muted: #4a4a4a;
    --text-light: #ffffff;
  }
  * { margin: 0; padding: 0; box-sizing: border-box; }
  html, body { width: 851px; height: 1200px; overflow: hidden; background: var(--paper); }
  .letterhead {
    position: relative;
    width: 851px;
    height: 1200px;
    background: var(--paper);
    font-family: "Montserrat", sans-serif;
    overflow: hidden;
  }
  .header-band { position: absolute; top: 0; left: 0; width: 851px; height: 150px; }
  .brand {
    position: absolute;
    top: 28px;
    left: 40px;
    display: flex;
    align-items: center;
    gap: 10px;
    color: var(--ink);
  }
  .brand-mark { width: 26px; height: 26px; border-radius: 50%; background: var(--ink); }
  .brand-name { font-weight: 800; font-size: 30px; letter-spacing: 0.5px; }
  .contact {
    position: absolute;
    left: 552px;
    top: 46px;
    color: var(--text-light);
    font-size: 14px;
    line-height: 17px;
    font-style: normal;
  }
  .contact-item { display: flex; align-items: flex-start; gap: 12px; margin-bottom: 14px; }
  .contact-item--center { align-items: center; }
  .contact-icon { width: 24px; height: 24px; flex: none; }
  .footer-flag { position: absolute; left: 0; bottom: 0; width: 380px; height: 200px; }
  .footer-rule {
    position: absolute;
    left: 160px;
    right: 0;
    top: 1110px;
    height: 2px;
    background: var(--rule);
  }
  .web-pill {
    position: absolute;
    top: 1093px;
    left: 366px;
    width: 232px;
    height: 34px;
    border-radius: 6px;
    background: var(--ink);
    color: var(--text-light);
    display: flex;
    align-items: center;
    justify-content: center;
    gap: 8px;
    font-size: 12.5px;
    font-weight: 500;
  }
  .web-icon { width: 18px; height: 18px; flex: none; }
  .company-details {
    position: absolute;
    left: 300px;
    right: 36px;
    top: 1142px;
    color: var(--muted);
    font-size: 10.5px;
    line-height: 17px;
    text-align: right;
  }
  .company-details strong { color: var(--ink); font-weight: 600; }
  .sep { color: var(--red); padding: 0 5px; }
</style>
</head>
<body>
<main class="letterhead">
  <svg class="header-band" viewBox="0 0 851 150" aria-hidden="true">
    <defs>
      <linearGradient id="bandRed" x1="0" y1="0" x2="1" y2="0">
        <stop offset="0" stop-color="#5e070b"/>
        <stop offset="0.5" stop-color="#a50f16"/>
        <stop offset="1" stop-color="#d0171f"/>
      </linearGradient>
    </defs>
    <polygon points="0,0 851,0 851,142 0,142" fill="var(--ink)"/>
    <polygon points="0,0 851,0 851,128 40,128 0,108" fill="url(#bandRed)"/>
    <polygon points="0,0 330,0 270,95 0,95" fill="var(--paper)"/>
  </svg>

  <div class="brand">
    <span class="brand-mark"></span>
    <span class="brand-name">VOLTRINA</span>
  </div>

  <address class="contact">
    <div class="contact-item">
      <svg class="contact-icon" viewBox="0 0 24 24" aria-hidden="true">
        <path d="M12 2a7 7 0 0 0-7 7c0 5 7 13 7 13s7-8 7-13a7 7 0 0 0-7-7z" fill="var(--red-icon)"/>
        <circle cx="12" cy="9" r="2.6" fill="#fff"/>
      </svg>
      <span>Amsel Strasse 7,<br>04683 Burgstädt, Germany</span>
    </div>
    <div class="contact-item contact-item--center">
      <svg class="contact-icon" viewBox="0 0 24 24" aria-hidden="true">
        <circle cx="12" cy="12" r="11" fill="var(--red-icon)"/>
        <rect x="6" y="8" width="12" height="8" rx="1" fill="#fff"/>
        <path d="M6.5 8.5 12 13l5.5-4.5" stroke="var(--red-icon)" stroke-width="1.3" fill="none"/>
      </svg>
      <span>info@voltrina-example.com</span>
    </div>
  </address>

  <svg class="footer-flag" viewBox="0 0 380 200" aria-hidden="true">
    <path d="M0 20 C120 20 210 90 250 200 L205 200 C170 110 95 62 0 62 Z" fill="var(--ink)"/>
    <path d="M0 62 C95 62 170 110 205 200 L160 200 C130 130 70 100 0 100 Z" fill="var(--red)"/>
    <path d="M0 100 C70 100 130 130 160 200 L118 200 C95 155 50 135 0 135 Z" fill="var(--gold)"/>
  </svg>

  <div class="footer-rule"></div>
  <div class="web-pill">
    <svg class="web-icon" viewBox="0 0 18 18" aria-hidden="true">
      <rect x="1" y="1" width="16" height="16" rx="3" fill="var(--red-icon)"/>
      <circle cx="9" cy="9" r="4.5" fill="none" stroke="#fff" stroke-width="1.2"/>
      <path d="M4.5 9h9M9 4.5v9" stroke="#fff" stroke-width="1"/>
    </svg>
    <span>http://voltrina-example.com</span>
  </div>

  <footer class="company-details">
    <p><strong>VOLTRINA UG</strong><span class="sep">|</span>Company Number: HRB 61508<span class="sep">|</span>VAT: DE5704168<span class="sep">|</span>EORI: 3041296587</p>
    <p>Norrfeld Bank<span class="sep">|</span>IBAN: DE421705238ß310482<span class="sep">|</span>Swift: KOLV3154802</p>
  </footer>
</main>
</body>
</html>
```